Belvin Merchants require a business card template and letterhead designed with our company logo. The business card needs to be in 2 dimension variations. The first being 84mm x 55mm and the second being 90mm x 55mm. The letterhead will be a standard A4 size of 210mm x 297mm.

At a minimum, the business card needs to show the company name (Belvin Merchants), persons first and last name (Peter walsh), phone number (+61 2 9555 8712), mobile number (+61 455 870 392), email address (peterw@[login to view URL]) and street address (47 Fernleigh Road Sydney NSW 2000). We tend to make notes on the back of our cards so whilst the back still needs to be visually appealing, some space to jot notes would be appreciated.

The letterhead needs to represent a nice balance between professional and creative. I have included three files. File 1 is the logo on a white, green and black background. File 2 and 3 are the fonts.

We require the winner to provide the designs in both Illustrator formats (font embedded), JPG, TIFF and BMP.

```html
<!DOCTYPE html>
<html lang="en">
<head>
<meta charset="utf-8">
<title>Belvin Merchants – Stationery</title>
<link href="https://fonts.googleapis.com/css2?family=Arimo:wght@400;700&family=Jost:wght@300;400&family=Libre+Baskerville:wght@700&display=swap" rel="stylesheet">
<style>
  :root{
    --stage-dark:#2c2c2c;
    --stage-light:#f7ef9f;
    --paper:#ffffff;
    --brand-green:#8cbf3f;
    --rule-green:#7aa33b;
    --card-green:#6a8b2b;
    --ink:#333333;
    --ink-soft:#5b5b5b;
    --ink-faint:#777777;
    --bar:#1d1d1d;
  }
  *{margin:0;padding:0;box-sizing:border-box}
  html,body{width:1200px;height:1057px;overflow:hidden}
  body{position:relative;background:var(--stage-light);font-family:"Arimo",Arial,sans-serif;color:var(--ink)}
  .stage-dark{position:absolute;left:0;top:0;width:849px;height:1057px;background:var(--stage-dark)}

  .letterhead{position:absolute;left:48px;top:27px;width:741px;height:962px;background:var(--paper)}
  .letterhead .brand{position:absolute;left:63px;top:66px;display:flex;align-items:center;gap:12px}
  .brand-dot{width:34px;height:34px;border-radius:50%;background:var(--brand-green)}
  .brand-name{font-family:"Jost",sans-serif;font-weight:300;color:var(--brand-green);font-size:31px;letter-spacing:3px;line-height:1}
  .letterhead .head-rule{position:absolute;left:53px;top:132px;width:350px;height:1px;background:var(--rule-green)}
  .address{position:absolute;left:483px;top:27px;font-size:14px;line-height:21px;color:#222}
  .address strong{font-weight:700}
  .salutation{position:absolute;left:125px;top:256px;font-size:13px;font-weight:700;color:var(--ink-soft)}
  .body-text{position:absolute;left:125px;top:332px;width:480px;font-size:9.4px;line-height:17.2px;color:#444}
  .body-text p+p{margin-top:17px}
  .signoff{position:absolute;left:125px;top:723px;font-size:10px;color:var(--ink-faint)}
  .footer-bar{position:absolute;left:11px;top:937px;width:720px;height:16px;background:var(--bar)}
  .footer-bar span{position:absolute;left:198px;top:2px;font-size:9px;color:#fff}

  .card{position:absolute;width:261px;height:149px}
  .card-front{left:876px;top:41px;background:var(--paper);box-shadow:0 1px 3px rgba(0,0,0,.25)}
  .card-front .edge{position:absolute;right:0;top:0;width:14px;height:100%;background:var(--bar)}
  .card-front .brand-name{position:absolute;left:8px;top:17px;font-size:14px;letter-spacing:1.5px}
  .card-front .person{position:absolute;left:8px;top:91px;font-family:"Libre Baskerville",serif;font-weight:700;font-size:10.5px;color:var(--ink-soft)}
  .card-front .role{position:absolute;left:8px;top:106px;font-size:5px;color:var(--brand-green)}
  .card-front .company{position:absolute;left:135px;top:77px;font-family:"Jost",sans-serif;font-weight:300;font-size:16px;color:var(--rule-green)}
  .contacts{position:absolute;left:124px;top:106px;list-style:none;font-size:6.3px;line-height:8.6px;color:#444}
  .contacts li{display:flex;align-items:center;gap:3px}
  .contacts svg{width:6px;height:6px;flex:none}
  .contacts .plain{padding-left:9px}
  .card-back{left:879px;top:203px;height:148px;background:var(--card-green);box-shadow:0 1px 3px rgba(0,0,0,.25);display:flex;align-items:center;justify-content:center}
  .card-back .brand-name{color:#fff;font-size:21px;letter-spacing:2.5px}
</style>
</head>
<body>
  <div class="stage-dark"></div>

  <section class="letterhead">
    <div class="brand"><span class="brand-dot"></span><span class="brand-name">BELVIN MERCHANTS</span></div>
    <div class="head-rule"></div>
    <address class="address" style="font-style:normal">
      <strong>Company Address:</strong><br>
      Belvin Merchants<br>
      47 Fernleigh Road Sydney NSW 2000<br>
      +61 2 9555 8712
    </address>

    <p class="salutation">Dear Mr. Harlow</p>

    <div class="body-text">
      <p>Lorem ipsum dolor sit amet, consectetur adipiscing elit. Vestibulum adipiscing felis ac tortor consectetur feugiat. Etiam malesuada sodales eros ut ornare. Sed lorem eros, mattis id pretium ut, faucibus sit amet quam. Nullam consectetur ultricies ipsum, fringilla porttitor erat ornare at. Sed sit amet dui vel sapien ultrices vulputate. In hac habitasse platea dictumst. Nam est nisi, rhoncus at sagittis a, porttitor adipiscing nulla. Vivamus placerat felis ultrices quam iaculis eget dignissim felis egestas. Integer nec molestie lorem. Sed odio tellus, vulputate sed laoreet non, vulputate id justo. Etiam suscipit, odio vel auctor dictum, felis turpis ullamcorper neque, quis sodales risus metus in magna. Morbi pellentesque justo et quam laoreet facilisis. Aenean placerat, urna ornare aliquet tincidunt, lorem justo molestie ligula, id placerat est metus nec lectus. Nullam eu ipsum quis turpis tristique iaculis rutrum nec nibh. Phasellus risus eros, semper sit amet faucibus sit amet, laoreet et neque. Donec eros sem, viverra dictum faucibus quis, ullamcorper tincidunt nulla.</p>
      <p>Aenean ut congue tellus. Class aptent taciti sociosqu ad litora torquent per conubia nostra, per inceptos himenaeos. Sed facilisis, velit tincidunt pharetra fermentum, urna tortor iaculis erat, vitae sollicitudin leo mauris quis mi. Cras malesuada sem ac ipsum sagittis ultrices. Mauris fermentum porttitor nisi, eu facilisis lorem consectetur et. Suspendisse est elit, scelerisque ac euismod id, scelerisque viverra odio. Nullam scelerisque metus in eros semper congue. Fusce a fermentum est. Ut ac leo dolor. Quisque dignissim mauris a neque luctus pretium ultrices risus sagittis. Aenean quam massa, rutrum ac hendrerit eu, interdum eu nulla. Curabitur a velit mauris, sed porta eros. Cras id egestas sapien. Proin non metus eget felis eleifend adipiscing. Nunc malesuada pharetra blandit.</p>
    </div>

    <p class="signoff">Your sincerely</p>

    <div class="footer-bar"><span>www.belvinmerchants.net</span></div>
  </section>

  <section class="card card-front">
    <span class="brand-name">BELVIN MERCHANTS</span>
    <p class="person">PETER WALSH</p>
    <p class="role">Director</p>
    <p class="company">Belvin Merchants</p>
    <ul class="contacts">
      <li><svg viewBox="0 0 10 10"><path d="M5 0a3.5 3.5 0 0 0-3.5 3.5C1.5 6 5 10 5 10s3.5-4 3.5-6.5A3.5 3.5 0 0 0 5 0zm0 5a1.5 1.5 0 1 1 0-3 1.5 1.5 0 0 1 0 3z" fill="#333"/></svg>47 Fernleigh Road Sydney NSW 2000</li>
      <li><svg viewBox="0 0 10 10"><rect x="0.5" y="2" width="9" height="6" fill="none" stroke="#333"/><path d="M.5 2 5 5.5 9.5 2" fill="none" stroke="#333"/></svg>peterw@belvinmerchants.com.au</li>
      <li><svg viewBox="0 0 10 10"><path d="M2 0.5 4 3 3 4.5C4 6 4.5 6.5 5.5 7L7 6l2.5 2L8 9.5C4 9.5 0.5 6 0.5 2z" fill="#333"/></svg>+61 2 9555 8712</li>
      <li class="plain">+61 455 870 392</li>
    </ul>
    <div class="edge"></div>
  </section>

  <section class="card card-back">
    <span class="brand-name">BELVIN MERCHANTS</span>
  </section>
</body>
</html>
```